Name for Roofing Company

We are a company that specialises in supply and installation of metal roofing to Commercial and Domestic buildings in Perth Western Australia. We are looking for someone to come up with a name that is catch innovative and marketable.

```html
<!DOCTYPE html>
<html lang="en">
<head>
<meta charset="UTF-8">
<title>Vantor Roofs — Name Proposal</title>
<link rel="stylesheet" href="https://fonts.googleapis.com/css2?family=Carlito:wght@400&display=swap">
<style>
  :root {
    --brand-red: #a80000;
    --ink: #262626;
    --paper-top: #ffffff;
    --paper-mid: #f0f0f0;
    --paper-bottom: #d6d6d6;
  }
  html, body {
    margin: 0;
    padding: 0;
    width: 1200px;
    height: 1200px;
    overflow: hidden;
  }
  .name-card {
    position: relative;
    width: 1200px;
    height: 1200px;
    background: linear-gradient(180deg, var(--paper-top) 0%, var(--paper-mid) 45%, var(--paper-bottom) 100%);
    overflow: hidden;
  }
  .name-card__block {
    position: absolute;
    left: 102px;
    top: 0;
    width: 990px;
    height: 532px;
    background: var(--brand-red);
  }
  .name-card__title {
    position: absolute;
    left: 116px;
    top: 634px;
    margin: 0;
    font-family: "Carlito", "Calibri", sans-serif;
    font-weight: 400;
    font-size: 170px;
    line-height: 1;
    color: var(--ink);
    letter-spacing: 0;
    white-space: nowrap;
  }
  .name-card__rule {
    position: absolute;
    left: 102px;
    top: 1079px;
    width: 990px;
    height: 3px;
    background: var(--brand-red);
  }
</style>
</head>
<body>
  <main class="name-card">
    <div class="name-card__block"></div>
    <h1 class="name-card__title">Vantor Roofs</h1>
    <div class="name-card__rule"></div>
  </main>
</body>
</html>
```